Flyer for Healthcare Provider -- Sleep Disorders
Sleep Scoring Services
Need Help Scoring
Flyer to be sent out to potential clients
Health
Doctors, healthcare professionals, healthcare administrators, CEOs, sleep lab managers, etc
- Need the flyer to have a strong medical and corporate feel
- Need to sell our services
Text for flyer
Company logo

```html
<!DOCTYPE html>
<html lang="en">
<head>
<meta charset="utf-8">
<title>Restwell Analytics – Priority Scoring Flyer and Stationery</title>
<link href="https://fonts.googleapis.com/css2?family=PT+Sans:wght@400;700&display=swap" rel="stylesheet">
<style>
  :root{
    --page-bg:#e9e6e2;
    --paper:#ffffff;
    --blue:#1d62a8;
    --blue-deep:#0f3c74;
    --blue-light:#4a93d6;
    --ink:#2b3440;
    --muted:#5d6670;
    --accent:#f4c64a;
    --rule:#c9ced4;
    --ornament:#eef0f2;
  }
  *{box-sizing:border-box;margin:0;padding:0}
  html,body{width:1200px;height:835px;overflow:hidden}
  body{background:var(--page-bg);font-family:"PT Sans",Arial,sans-serif;color:var(--ink);position:relative}

  /* ---------- Flyer ---------- */
  .flyer{position:absolute;left:40px;top:40px;width:530px;height:755px;background:var(--paper);overflow:hidden}
  .flyer-top{position:absolute;left:0;top:0;width:100%;height:368px}
  .intro{position:absolute;left:0;top:0;width:262px;height:100%;padding:0 18px 0 20px}
  .intro-head{background:var(--blue);color:#fff;font-size:22px;font-weight:700;margin:0 -18px 12px -20px;padding:10px 20px}
  .intro p{font-size:9.6px;line-height:1.4;margin-bottom:8px;color:var(--muted)}
  .signs{list-style:none;font-size:9.2px;line-height:1.35;color:var(--muted)}
  .signs li{position:relative;padding-left:10px;margin-bottom:4px}
  .signs li::before{content:"";position:absolute;left:0;top:5px;width:4px;height:4px;background:var(--blue)}
  .hero-photo{position:absolute;right:0;top:0;width:268px;height:100%;
    background:linear-gradient(160deg,#f3f1ee 0%,#e2d9cf 45%,#c9b8a6 100%)}
  .divider{position:absolute;left:0;top:368px;width:100%;height:12px;background:linear-gradient(90deg,var(--blue-deep),var(--blue-light))}

  .team-photo{position:absolute;left:0;top:380px;width:225px;height:310px;
    background:linear-gradient(180deg,#dfe6ee 0%,#9fb6cc 55%,#3f6f9d 100%)}
  .brand-band{position:absolute;left:0;top:690px;width:225px;height:65px;background:var(--blue-deep);
    display:flex;align-items:center;gap:10px;padding-left:18px}
  .brand-dot{width:22px;height:22px;border-radius:50%;background:#fff}
  .brand-name{color:#fff;font-size:19px;font-weight:700}

  .offer{position:absolute;left:225px;top:380px;width:305px;height:375px;
    background:linear-gradient(160deg,var(--blue) 0%,var(--blue-deep) 100%);color:#fff;padding:18px 16px 0 18px;overflow:hidden}
  .offer h2{font-size:26px;font-weight:700;line-height:1}
  .offer .lede{font-size:9px;color:#cfe2f5;margin:4px 0 9px}
  .offer p{font-size:8.8px;line-height:1.4;color:#e3eef9;margin-bottom:8px}
  .contact{text-align:center;margin-top:6px}
  .contact .call-in{font-size:9.5px;color:#e3eef9}
  .contact .phone{font-size:11.5px;font-weight:700;margin-top:4px;white-space:nowrap}
  .contact .web{font-size:12px;font-weight:700;margin-top:2px}
  .cta{text-align:center;margin-top:14px}
  .cta .small{font-size:12px;color:#e3eef9}
  .cta .big{font-size:26px;color:var(--accent);line-height:1.1}
  .cta .big b{font-size:32px}

  /* ---------- Letter sheet ---------- */
  .letter{position:absolute;left:610px;top:30px;width:310px;height:540px;background:var(--paper)}
  .discount{position:absolute;left:0;width:100%;text-align:center;font-size:26px;color:#3a3a3a;letter-spacing:.5px}
  .letter .discount{top:205px}
  .letter-ornament{position:absolute;left:20px;top:245px;width:270px;height:40px;
    background:linear-gradient(90deg,var(--paper),var(--ornament) 50%,var(--paper))}

  /* ---------- Envelope ---------- */
  .envelope{position:absolute;left:860px;top:590px;width:300px;height:218px;background:var(--paper)}
  .envelope svg{position:absolute;left:0;top:0}
  .envelope .discount{top:58px;font-size:24px}
</style>
</head>
<body>

<section class="flyer" aria-label="Priority Scoring flyer">
  <div class="flyer-top">
    <div class="intro">
      <h1 class="intro-head">Need help Scoring?</h1>
      <p>Restwell Analytics provides the highest quality and most cost effective scoring services to the sleep medicine industry.</p>
      <p>How do you know when the time is right to hire a professional scoring service? Below are a few telltale signs that your sleep laboratory is ready for a scoring service provider.</p>
      <ul class="signs">
        <li>Your sleep laboratory repeatedly has a backlog of sleep studies</li>
        <li>It takes longer than 3 business days to have sleep studies scored</li>
        <li>You are short staffed – vacation, sick days, maternity and unexpected departures impact productivity</li>
        <li>Your sleep laboratory has limited or no RPSGTs on staff</li>
        <li>It is necessary for your sleep technologists to reduce labor and control operating costs</li>
        <li>Quality assurance with internal scorers has been brought into question</li>
      </ul>
    </div>
    <div class="hero-photo" role="img" aria-label="Photo of a smiling professional woman"></div>
  </div>
  <div class="divider"></div>

  <div class="team-photo" role="img" aria-label="Photo of a medical team: doctor and two clinicians"></div>
  <div class="brand-band">
    <span class="brand-dot"></span>
    <span class="brand-name">Restwell Analytics</span>
  </div>

  <div class="offer">
    <h2>Priority Scoring</h2>
    <div class="lede">For patient records that need faster than standard turnaround</div>
    <p>There are always some patients that require immediate attention. Our Priority Scoring option delivers your scored studies within hours so your physicians can act quickly, review results sooner and keep every patient moving through care without added delay.</p>
    <p>Sleep centers across the country trust our team of registered scorers to deliver accurate, consistent results. Let us help you manage volume and reduce costs.</p>
    <div class="contact">
      <div class="call-in">For a complimentary evaluation of your current scoring practices, contact us:</div>
      <div class="phone">1-800-555-0147 | info@restwellanalytics.com</div>
      <div class="web">www.restwellanalytics.com</div>
    </div>
    <div class="cta">
      <div class="small">Call today and sign up for a</div>
      <div class="big"><b>10%</b> DISCOUNT OFF</div>
      <div class="small">your first 50 sleep studies.</div>
    </div>
  </div>
</section>

<section class="letter" aria-label="Discount letter sheet">
  <div class="discount">10% DISCOUNT</div>
  <div class="letter-ornament" role="img" aria-label="Thin heartbeat line ornament ending in a circular emblem"></div>
</section>

<section class="envelope" aria-label="Discount envelope">
  <svg width="300" height="218" viewBox="0 0 300 218" aria-hidden="true">
    <polyline points="0,0 150,40 300,0" fill="none" stroke="var(--rule)" stroke-width="1"/>
  </svg>
  <div class="discount">10% DISCOUNT</div>
</section>

</body>
</html>
```